K7 Digital Stationery Design Project

We are looking to have stationary designs created for our company branding materials. We are looking for the following to be created.
1. Business Cards (front & back)
2. Letterhead
3. Envelopes #10
We are a new web design, development and marketing firm. Primary color scheme is desired to be blue/grey/white. This web start-up is owned and operated by individuals with 15+ years experience each in the industry so should not look as though it is a start-up by young/inexperienced individuals.
We build website & custom applications/software. In addition we provide the full spectrum of web marketing solutions including SEO, PPC, Social Media, Branding, Content Marketing and PR.
Please let us know if you have any questions. Looking forward to seeing all the amazing design ideas.
Attached is our logo.
Thanks!
Target Market(s)
Company will be nearly 100% business to business sales. Looking to work with companies that are already established, with a website, who want to take their website and/or online marketing efforts to the next level.
Industry/Entity Type
Marketing
Look and feel

```html
<!DOCTYPE html>
<html lang="en">
<head>
<meta charset="utf-8">
<title>K7 Digital — Stationery Set</title>
<link href="https://fonts.googleapis.com/css2?family=Jost:wght@400;500;700&display=swap" rel="stylesheet">
<style>
  :root {
    --blue: #1f8fd4;
    --blue-deep: #1d6fc0;
    --ink: #3a3b3d;
    --ink-soft: #6a6c70;
    --paper: #ffffff;
    --stock-light: #f4f5f6;
    --stock-grey: #dfe1e4;
    --backdrop: #eceae6;
    --edge: rgba(0,0,0,0.12);
  }
  * { box-sizing: border-box; margin: 0; padding: 0; }
  html, body { width: 1200px; height: 900px; overflow: hidden; }
  body {
    position: relative;
    background: var(--backdrop);
    font-family: "Jost", "Futura", sans-serif;
    color: var(--ink);
  }
  .piece {
    position: absolute;
    background: var(--paper);
    box-shadow: 0 1px 3px var(--edge), 0 6px 14px rgba(0,0,0,0.06);
    overflow: hidden;
  }
  .piece--grey {
    background: radial-gradient(ellipse at 55% 45%, var(--stock-light) 0%, var(--stock-grey) 100%);
  }

  /* Lockup: plain dot + company name + tagline */
  .lockup { display: flex; align-items: center; gap: 8px; }
  .lockup__dot { border-radius: 50%; background: var(--blue); flex: none; }
  .lockup__name { font-weight: 700; color: var(--ink); text-transform: uppercase; line-height: 1; letter-spacing: 0.01em; }
  .lockup__tagline { font-weight: 500; color: var(--ink); line-height: 1.1; margin-top: 2px; }

  /* Large brand feature */
  .feature { position: absolute; left: 50%; top: 50%; transform: translate(-50%, -50%); display: flex; flex-direction: column; align-items: center; gap: 14px; }
  .feature__dot { border-radius: 50%; background: linear-gradient(180deg, var(--blue), var(--blue-deep)); }
  .feature__name { font-weight: 500; color: var(--blue-deep); white-space: nowrap; line-height: 1; }

  .contact { font-size: 7px; line-height: 1.45; color: var(--ink); }
  .contact b { font-weight: 500; display: inline-block; width: 14px; }

  /* Letterhead */
  .letterhead { left: 40px; top: 40px; width: 340px; height: 440px; }
  .letterhead__header { position: absolute; left: 22px; top: 22px; display: flex; align-items: center; gap: 12px; }
  .letterhead__rule { width: 1px; height: 34px; background: var(--ink-soft); }

  /* Folder cover */
  .folder { left: 400px; top: 40px; width: 340px; height: 440px; }

  /* Envelopes */
  .envelope-back { left: 770px; top: 40px; width: 390px; height: 170px; }
  .envelope-back__flap { position: absolute; inset: 0; }
  .envelope-back__dot { position: absolute; left: 50%; top: 26px; width: 22px; height: 22px; margin-left: -11px; border-radius: 50%; background: var(--blue); }
  .envelope-back__sign { position: absolute; left: 0; right: 0; bottom: 18px; text-align: center; }
  .envelope-back__sign .lockup { justify-content: center; }

  .envelope-front { left: 770px; top: 235px; width: 390px; height: 170px; }
  .envelope-front .lockup { position: absolute; left: 14px; top: 16px; }
  .envelope-front__return { position: absolute; left: 14px; bottom: 12px; }

  /* Compliment card */
  .compliment { left: 40px; top: 510px; width: 400px; height: 240px; }
  .compliment__fold { position: absolute; left: 0; right: 0; top: 0; height: 6px; background: linear-gradient(180deg, rgba(0,0,0,0.06), transparent); }

  /* Business cards */
  .card-h { width: 250px; height: 143px; }
  .card-h--front { left: 470px; top: 510px; }
  .card-h--front .lockup { position: absolute; left: 22px; top: 50%; transform: translateY(-50%); }
  .card-h--back { left: 470px; top: 673px; }
  .card-h--back__dot { position: absolute; left: 26px; top: 34px; width: 18px; height: 18px; border-radius: 50%; background: var(--blue); }
  .card-h--back__body { position: absolute; left: 60px; top: 30px; border-left: 1px solid var(--ink-soft); padding-left: 8px; }

  .person__name { font-weight: 700; font-size: 9px; text-transform: uppercase; line-height: 1.1; }
  .person__role { font-weight: 500; font-size: 7px; text-transform: uppercase; margin-bottom: 8px; }

  .card-v { width: 160px; height: 280px; top: 510px; }
  .card-v--front { left: 750px; }
  .card-v--back { left: 935px; }
  .card-v--back .lockup { position: absolute; left: 14px; top: 44px; }
  .card-v--back__details { position: absolute; right: 14px; bottom: 34px; text-align: right; }
  .card-v--back__details .person__name { font-weight: 500; text-transform: none; font-size: 8px; }
  .card-v--back__details .person__role { text-transform: none; font-size: 7px; margin-bottom: 6px; }
</style>
</head>
<body>

  <!-- Letterhead -->
  <section class="piece letterhead" aria-label="Letterhead">
    <div class="letterhead__header">
      <div class="lockup">
        <span class="lockup__dot" style="width:16px;height:16px"></span>
        <div>
          <div class="lockup__name" style="font-size:13px">K7 Digital</div>
          <div class="lockup__tagline" style="font-size:6.5px">Web Design, Development and Marketing</div>
        </div>
      </div>
      <span class="letterhead__rule"></span>
      <div class="contact">
        <div><b>[P]</b>0100-555-0199</div>
        <div><b>[A]</b>Your Business Address, State, Zip Code</div>
        <div><b>[W]</b>www.k7digital.com</div>
      </div>
    </div>
  </section>

  <!-- Folder cover -->
  <section class="piece piece--grey folder" aria-label="Presentation folder cover">
    <div class="feature">
      <span class="feature__dot" style="width:36px;height:36px"></span>
      <span class="feature__name" style="font-size:38px">K7 Digital</span>
    </div>
  </section>

  <!-- Envelope back -->
  <section class="piece envelope-back" aria-label="Envelope back">
    <svg class="envelope-back__flap" viewBox="0 0 390 170" preserveAspectRatio="none" aria-hidden="true">
      <polyline points="0,0 12,24 160,58 230,58 378,24 390,0" fill="#f7f7f8" stroke="#cfd1d4" stroke-width="1"/>
    </svg>
    <span class="envelope-back__dot"></span>
    <div class="envelope-back__sign">
      <div class="lockup">
        <div>
          <div class="lockup__name" style="font-size:13px">K7 Digital</div>
          <div class="lockup__tagline" style="font-size:6.5px">Web Design, Development and Marketing</div>
        </div>
      </div>
    </div>
  </section>

  <!-- Envelope front -->
  <section class="piece piece--grey envelope-front" aria-label="Envelope front">
    <div class="lockup">
      <span class="lockup__dot" style="width:20px;height:20px"></span>
      <div>
        <div class="lockup__name" style="font-size:14px">K7 Digital</div>
        <div class="lockup__tagline" style="font-size:6.5px">Web Design, Development and Marketing</div>
      </div>
    </div>
    <div class="contact envelope-front__return">
      <div>Your Business Address, City, State, Zip Code</div>
      <div>0100-555-0199&nbsp;&nbsp;&nbsp;&nbsp;&nbsp;www.k7digital.com</div>
    </div>
  </section>

  <!-- Compliment card -->
  <section class="piece compliment" aria-label="Folded compliment card">
    <span class="compliment__fold"></span>
    <div class="feature">
      <span class="feature__dot" style="width:30px;height:30px"></span>
      <span class="feature__name" style="font-size:34px">K7 Digital</span>
    </div>
  </section>

  <!-- Business card, landscape front -->
  <section class="piece piece--grey card-h card-h--front" aria-label="Business card front">
    <div class="lockup">
      <span class="lockup__dot" style="width:20px;height:20px"></span>
      <div>
        <div class="lockup__name" style="font-size:16px">K7 Digital</div>
        <div class="lockup__tagline" style="font-size:7px">Web Design, Development and Marketing</div>
      </div>
    </div>
  </section>

  <!-- Business card, landscape back -->
  <section class="piece card-h card-h--back" aria-label="Business card back">
    <span class="card-h--back__dot"></span>
    <div class="card-h--back__body">
      <div class="person__name">Mr. Dale Hoskins</div>
      <div class="person__role">Head Designer</div>
      <div class="contact">
        <div>0100-555-0199</div>
        <div>hello@k7digital.com</div>
        <div>Your Business Address, State, Zip Code</div>
        <div>www.k7digital.com</div>
      </div>
    </div>
  </section>

  <!-- Business card, portrait front -->
  <section class="piece piece--grey card-v card-v--front" aria-label="Business card front, portrait">
    <div class="feature">
      <span class="feature__dot" style="width:20px;height:20px"></span>
      <span class="feature__name" style="font-size:22px">K7 Digital</span>
    </div>
  </section>

  <!-- Business card, portrait back -->
  <section class="piece card-v card-v--back" aria-label="Business card back, portrait">
    <div class="lockup">
      <span class="lockup__dot" style="width:16px;height:16px"></span>
      <div>
        <div class="lockup__name" style="font-size:12px">K7 Digital</div>
        <div class="lockup__tagline" style="font-size:5.5px">Web Design, Development and Marketing</div>
      </div>
    </div>
    <div class="card-v--back__details">
      <div class="person__name">Mr. Dale Hoskins</div>
      <div class="person__role">Head Designer</div>
      <div class="contact" style="font-size:6px">
        <div>Your Business Address</div>
        <div>City, State, Zip Code</div>
        <div style="margin-top:4px">(P) 0100-555-0199</div>
        <div>(F) 0100-555-0198</div>
        <div style="margin-top:4px">hello@k7digital.com</div>
        <div>www.k7digital.com</div>
      </div>
    </div>
  </section>

</body>
</html>
```